New Infusion Pharmacy needs Business Card design

Hello!

We are Verant Infusion Pharmacy, are we are looking for a two sided, clean and modern business card.

First, let me give you a little bit about what an infusion pharmacy does...
We compound and fill prescriptions for drugs that are injectable, meaning that they are administered via an IV bag or a syringe. Basically anything that is too advanced for a normal pill pharmacy to fill. We compound everything in our state of the art clean room, then deliver it directly to the patients home. We have an outside sales force that markets to hospitals, home health agencies, and doctor's offices.

as for the business card...
We are looking for a clean, modern card. our colors are in our logo, kind of a light bule and a darker blue. We do really like the rounded corners on the card. Also, we would like the back of the card to be the reverse colors of the front, for example, if the front of the card has a light background, then the back of the card will have a dark background.

On the back side of the card we want to have our logo, then list some of the services we offer:
-IVIG
-TPN
-Enteral Nutrition
-IV Antibiotics
-IV Hydration
-Blood Factors
-Chemotherapy
-Pain Management

Our logo is uploaded in .psd format, if you need a different format let me know and i'll throw it up here.

Thank you so much!!

Industry/Entity Type

Pharmacy

Requirements
Must have
• Front of Card: (no particular order, please arrange in whatever way you think looks best!)
-Employee Name
-Title
-Office Phone #
-Cell Phone #
-Fax #
-email address - marlo@verantcareinfuse.com
-office address - 4127 Delmore St. Larkfield, CA 90418
-Web Site - www.verantcareinfuse.com

```html
<!DOCTYPE html>
<html lang="en">
<head>
<meta charset="utf-8">
<title>Verant Infusion Pharmacy – Business Card</title>
<link href="https://fonts.googleapis.com/css2?family=Open+Sans:wght@400;600;700&display=swap" rel="stylesheet">
<style>
  :root {
    --canvas: #e4e6e8;
    --card-light: #ffffff;
    --card-blue: #1e9fca;
    --brand-dark: #0f5d7a;
    --ink: #333a3f;
    --white: #ffffff;
    --rule-dark: #177fa3;
  }
  * { box-sizing: border-box; margin: 0; padding: 0; }
  html, body { width: 1200px; height: 900px; overflow: hidden; }
  body {
    background: var(--canvas);
    font-family: "Open Sans", Arial, sans-serif;
    position: relative;
  }
  .card {
    position: absolute;
    width: 600px;
    height: 343px;
    border-radius: 30px;
    box-shadow: 0 10px 28px rgba(0,0,0,0.18);
    overflow: hidden;
  }

  /* Back of card */
  .card-back {
    left: 420px;
    top: 60px;
    background: var(--card-blue);
    color: var(--white);
    text-align: center;
    padding: 58px 50px 0;
  }
  .card-back .wordmark-name {
    font-size: 84px;
    font-weight: 600;
    letter-spacing: 2px;
    line-height: 1;
  }
  .card-back .wordmark-tag {
    font-size: 22px;
    font-weight: 600;
    letter-spacing: 9px;
    margin-top: 6px;
  }
  .card-back .divider {
    height: 1px;
    background: var(--rule-dark);
    margin: 20px 0 18px;
  }
  .services {
    font-size: 19px;
    line-height: 1.4;
  }

  /* Front of card */
  .card-front {
    left: 180px;
    top: 470px;
    background: var(--card-light);
    color: var(--ink);
  }
  .card-front .wordmark {
    position: absolute;
    right: 34px;
    top: 38px;
    text-align: right;
    color: var(--brand-dark);
  }
  .card-front .wordmark-name {
    font-size: 64px;
    font-weight: 600;
    letter-spacing: 2px;
    line-height: 1;
  }
  .card-front .wordmark-tag {
    font-size: 16px;
    font-weight: 600;
    letter-spacing: 6px;
    margin-top: 4px;
  }
  .person {
    position: absolute;
    left: 30px;
    top: 162px;
  }
  .person-name {
    font-size: 26px;
    font-weight: 600;
    color: var(--brand-dark);
    letter-spacing: 0.5px;
  }
  .person-title {
    font-size: 16px;
    margin-top: 1px;
  }
  .contact {
    position: absolute;
    left: 30px;
    right: 20px;
    top: 236px;
    font-size: 17px;
    line-height: 1.45;
    white-space: nowrap;
  }
  .contact .label { font-weight: 700; color: var(--brand-dark); }
  .contact .site { font-weight: 700; }
  .contact .address { margin-top: 6px; }
</style>
</head>
<body>

  <section class="card card-back" aria-label="Business card back">
    <div class="wordmark">
      <div class="wordmark-name">VERANT</div>
      <div class="wordmark-tag">INFUSION PHARMACY</div>
    </div>
    <div class="divider"></div>
    <p class="services">
      IVIG • TPN • Enteral Nutrition • IV Antibiotics<br>
      IV Hydration • Blood Factors • Chemotherapy<br>
      Pain Management
    </p>
  </section>

  <section class="card card-front" aria-label="Business card front">
    <div class="wordmark">
      <div class="wordmark-name">VERANT</div>
      <div class="wordmark-tag">INFUSION PHARMACY</div>
    </div>
    <div class="person">
      <div class="person-name">MARLO HENSLEY</div>
      <div class="person-title">Operation Manager</div>
    </div>
    <div class="contact">
      <div><span class="label">T</span>: (221) 48 512 30 64 | <span class="label">F</span>: (221) 62 704 18 53 | <span class="label">M</span>: (221) 62 704 18 53</div>
      <div><span class="label">E</span>: marlo@verantcareinfuse.com | <span class="site">www.verantcareinfuse.com</span></div>
      <div class="address">4127 Delmore St. Larkfield, CA 90418</div>
    </div>
  </section>

</body>
</html>
```